Lumo Vance IT company Soho london Stationary

We've just had a new logo designed on Gallow Pier and we now need some Stationary to go with it.
We're a small IT support firm supporting Design companies in Soho London. Most of our clients work on Vorls and a relatively creative so we want a relatively informal design on our stationary to reflect this.
We'd like to stick with the green in the logo but we're not adverse to adding another few colours to the palette.
Please see the attached file for our logo and not our website.

It Company

```html
<!DOCTYPE html>
<html lang="en">
<head>
<meta charset="utf-8">
<title>Lumo Vance – Stationery</title>
<link rel="stylesheet" href="https://fonts.googleapis.com/css2?family=Questrial&display=swap">
<style>
  :root {
    --board: #d8dad9;
    --paper: #ffffff;
    --green: #c3d82e;
    --ink: #2b2b2b;
    --shadow: rgba(0, 0, 0, 0.28);
    --font: "Questrial", "Century Gothic", sans-serif;
  }
  html, body {
    margin: 0;
    padding: 0;
    overflow: hidden;
  }
  .board {
    position: relative;
    width: 1200px;
    height: 901px;
    background: var(--board);
    font-family: var(--font);
    color: var(--ink);
    overflow: hidden;
  }
  .sheet {
    position: absolute;
    background: var(--paper);
    box-shadow: 0 2px 5px var(--shadow);
    overflow: hidden;
  }
  .wordmark {
    position: absolute;
    margin: 0;
    color: var(--green);
    font-family: var(--font);
    font-weight: 400;
    white-space: nowrap;
    line-height: 1;
    letter-spacing: 0.01em;
  }
  .brand-band {
    position: absolute;
    left: 0;
    right: 0;
    bottom: 0;
    background: var(--green);
  }

  /* Business card – front */
  .card-front { left: 109px; top: 234px; width: 255px; height: 143px; }
  .card-front .wordmark {
    left: 0; right: 0; top: 60px;
    text-align: center;
    font-size: 24px;
  }

  /* Business card – back */
  .card-back { left: 109px; top: 412px; width: 255px; height: 143px; }
  .card-back .wordmark { left: 12px; top: 18px; font-size: 19px; }
  .card-back .brand-band { height: 13px; }
  .holder {
    position: absolute;
    right: 135px;
    top: 59px;
    text-align: right;
    font-size: 7px;
    line-height: 8.5px;
  }
  .holder .name { font-weight: 700; }
  .card-contact {
    position: absolute;
    left: 144px;
    top: 59px;
    font-size: 7px;
    line-height: 8.5px;
  }
  .card-contact p { margin: 0 0 8px; }
  .card-contact .web { font-weight: 700; }

  /* Letterhead */
  .letterhead { left: 453px; top: 25px; width: 595px; height: 843px; }
  .letterhead .wordmark {
    left: 0; right: 0; top: 50px;
    text-align: center;
    font-size: 42px;
  }
  .letterhead-footer {
    position: absolute;
    left: 0; right: 0; top: 796px;
    text-align: center;
    font-size: 10.5px;
    line-height: 13px;
  }
  .letterhead-footer p { margin: 0; }
  .letterhead-footer .web { font-weight: 700; }
  .letterhead .brand-band { height: 18px; }
</style>
</head>
<body>
<main class="board">

  <section class="sheet card-front" aria-label="Business card front">
    <p class="wordmark">Lumo Vance</p>
  </section>

  <section class="sheet card-back" aria-label="Business card back">
    <p class="wordmark">Lumo Vance</p>
    <div class="holder">
      <div class="name">Sample Name</div>
      <div class="role">title</div>
    </div>
    <div class="card-contact">
      <p>Lumo Vance Ltd.<br>42 Carrow Lane<br>London, W1 4QT</p>
      <p>Phone: 0203 555 0148<br>email: info@lumo-vance.it<br><span class="web">http://lumo-vance.it</span></p>
    </div>
    <div class="brand-band"></div>
  </section>

  <section class="sheet letterhead" aria-label="Letterhead">
    <p class="wordmark">Lumo Vance</p>
    <footer class="letterhead-footer">
      <p>Lumo Vance Ltd. | 42 Carrow Lane | London, W1 4QT</p>
      <p>Phone: 0203 555 0148 | email: info@lumo-vance.it | <span class="web">http://lumo-vance.it</span></p>
    </footer>
    <div class="brand-band"></div>
  </section>

</main>
</body>
</html>
```